K&T Fixit and Rebuild general contracting business card design

I already have a logo that I want to use and I need a card that uses that logo and color scheme on the front with the address phone numbers and email and on the back a place for technicians to write in their name and phone number when they hand it out. It will need the License number of License #KTFXTRB318QN.
It should say General Contractor under the company name. The address is
4417 NE 3rd Ave, Ste D246
Quillmont, OR 97999
www.kandtfixitandrebuild.example
office@kandtfixitandrebuild.example
555-555-0182 is the telephone number
555-555-0149 is the fax number

Target Market(s)

Homeowners needing remodel work or repairs in their home.

Industry/Entity Type

Construction

Contact Information for Business Card

Business name, address, phone number, license number, fax number, email, and website on the front and a place to fill in technician's name and number

Font styles to use
Serif

Requirements
Must have
• Business name, address, phone number, license number, fax number, email, and website on the front and a place to fill in technician's name and number
Nice to have
• I uploaded an example of a front that is good.
Should not have
• Froo froo or extra embellishments.

```html
<!DOCTYPE html>
<html lang="en">
<head>
<meta charset="utf-8">
<title>K&amp;T Fixit and Rebuild — Business Card</title>
<link href="https://fonts.googleapis.com/css2?family=Montserrat:wght@400;500;600;700&display=swap" rel="stylesheet">
<style>
  :root {
    --stage: #1e1e1f;
    --paper: #ffffff;
    --wood-light: #d9782f;
    --wood-mid: #c4621f;
    --wood-dark: #a94f15;
    --brand: #b5602d;
    --ink: #1c1c1c;
    --rule: #333333;
    --on-wood: #ffffff;
  }
  * { box-sizing: border-box; margin: 0; padding: 0; }
  html, body {
    width: 1200px; height: 780px; overflow: hidden;
    background: var(--stage);
    font-family: "Montserrat", sans-serif;
  }
  .sheet {
    width: 1200px; height: 780px;
    display: flex; align-items: center; justify-content: center; gap: 40px;
  }
  .card {
    position: relative;
    width: 540px; height: 310px;
    background: var(--paper);
    border-radius: 22px;
    overflow: hidden;
  }
  .wood-band {
    position: absolute; left: 0; right: 0; bottom: 0;
    background: linear-gradient(100deg, var(--wood-dark) 0%, var(--wood-mid) 35%, var(--wood-light) 60%, var(--wood-mid) 85%, var(--wood-dark) 100%);
  }
  .brand-name {
    display: flex; align-items: center; gap: 8px;
    color: var(--brand);
    font-weight: 700;
    text-transform: uppercase;
    line-height: 1.05;
  }
  .brand-mark {
    width: 12px; height: 12px; background: var(--brand); flex: none;
  }

  /* Back */
  .card--back .wood-band { height: 72px; }
  .card--back .brand-name {
    position: absolute; left: 46px; top: 92px; width: 180px;
    font-size: 24px;
  }
  .card--back .divider {
    position: absolute; left: 240px; top: 62px; width: 1px; height: 150px;
    background: var(--rule);
  }
  .write-lines {
    position: absolute; left: 285px; top: 78px; width: 210px;
    display: flex; flex-direction: column; gap: 38px;
  }
  .write-line { border-top: 1.5px dotted var(--rule); height: 0; }
  .license {
    position: absolute; left: 0; right: 0; bottom: 0; height: 72px;
    display: flex; align-items: center; justify-content: center;
    color: var(--on-wood);
    font-size: 14px; font-weight: 500; letter-spacing: 5px;
  }

  /* Front */
  .card--front .wood-band { height: 140px; }
  .card--front .brand-name {
    position: absolute; left: 0; right: 0; top: 52px;
    justify-content: center;
    font-size: 26px;
  }
  .tagline {
    position: absolute; left: 0; right: 0; top: 118px;
    text-align: center;
    color: var(--ink);
    font-size: 13px; font-weight: 500; letter-spacing: 9px;
  }
  .contacts {
    position: absolute; left: 26px; bottom: 18px;
    list-style: none;
    display: flex; flex-direction: column; gap: 6px;
    color: var(--on-wood);
  }
  .contact {
    display: flex; align-items: center; gap: 9px;
    font-size: 11.5px; font-weight: 600;
  }
  .contact-icon {
    width: 19px; height: 19px; border-radius: 50%;
    background: var(--on-wood);
    display: flex; align-items: center; justify-content: center;
    flex: none;
  }
  .contact-icon svg { width: 11px; height: 11px; }
  .address {
    position: absolute; right: 26px; bottom: 96px;
    color: var(--on-wood);
    font-size: 11.5px; font-weight: 600;
    text-align: right; line-height: 1.35;
    font-style: normal;
  }
</style>
</head>
<body>
<main class="sheet">

  <section class="card card--back" aria-label="Card back">
    <div class="brand-name"><span class="brand-mark"></span><span>K&amp;T Fixit and Rebuild</span></div>
    <div class="divider"></div>
    <div class="write-lines">
      <div class="write-line"></div>
      <div class="write-line"></div>
      <div class="write-line"></div>
    </div>
    <div class="wood-band" role="img" aria-label="Wood grain texture band"></div>
    <p class="license">LICENSE #KTFXTRB318QN</p>
  </section>

  <section class="card card--front" aria-label="Card front">
    <div class="brand-name"><span class="brand-mark"></span><span>K&amp;T Fixit and Rebuild</span></div>
    <p class="tagline">GENERAL CONTRACTOR</p>
    <div class="wood-band" role="img" aria-label="Wood grain texture band"></div>
    <ul class="contacts">
      <li class="contact">
        <span class="contact-icon"><svg viewBox="0 0 24 24"><path fill="#c4621f" d="M6.6 10.8a15 15 0 0 0 6.6 6.6l2.2-2.2a1 1 0 0 1 1-.25 11.4 11.4 0 0 0 3.6.57 1 1 0 0 1 1 1V20a1 1 0 0 1-1 1A17 17 0 0 1 3 4a1 1 0 0 1 1-1h3.5a1 1 0 0 1 1 1c0 1.25.2 2.45.57 3.57a1 1 0 0 1-.25 1z"/></svg></span>
        <span>555-555-0182</span>
      </li>
      <li class="contact">
        <span class="contact-icon"><svg viewBox="0 0 24 24"><path fill="#c4621f" d="M7 3h8l3 3v4H7zM4 11h16a1 1 0 0 1 1 1v8a1 1 0 0 1-1 1H4a1 1 0 0 1-1-1v-8a1 1 0 0 1 1-1zm3 3v2h4v-2zm0 4v1h10v-1z"/></svg></span>
        <span>555-555-0149</span>
      </li>
      <li class="contact">
        <span class="contact-icon"><svg viewBox="0 0 24 24" fill="none" stroke="#c4621f" stroke-width="2"><circle cx="12" cy="12" r="9"/><path d="M3 12h18M12 3c3 3 3 15 0 18M12 3c-3 3-3 15 0 18"/></svg></span>
        <span>www.kandtfixitandrebuild.example</span>
      </li>
      <li class="contact">
        <span class="contact-icon"><svg viewBox="0 0 24 24"><path fill="#c4621f" d="M3 6h18v12H3zm1.5 1.5L12 13l7.5-5.5z" fill-rule="evenodd"/></svg></span>
        <span>office@kandtfixitandrebuild.example</span>
      </li>
    </ul>
    <address class="address">4417 NE 3rd Ave, Ste D246<br>Quillmont, OR 97999</address>
  </section>

</main>
</body>
</html>
```